PelvixRails: A Swiss railway modelling online shop

I am the developer of PelvixRails, a railway modelling online shop (https://www.pelvixrails-demo.example) originally developed back in 2004. Today the website needs a complete back-end refresh, which is mostly completed on my side. However I am lacking skills in design, hence my request for support.
The owner of PelvixRails wants to modernize the overall design. He wishes to have it sober, modern and responsive. So you have pretty much "carte blanche" in terms of proposal, the only constraint is to keep the logo as is.
Some products can have variants (e.g. a locomotive can be sold in direct or alternating current), as you can see in the screenshot or when navigating his website.
The current navigation with Brand > Scale > Category > Company can remain, however we would want eventually a page with facet navigation that make it easier to search for a specific article.

```html
<!DOCTYPE html>
<html lang="en">
<head>
<meta charset="utf-8">
<title>PelvixRails – Locomotives</title>
<link href="https://fonts.googleapis.com/css2?family=Inter:wght@400;500;600&display=swap" rel="stylesheet">
<style>
:root{
  --header-bg:#fffbd3;
  --accent:#ea4340;
  --indigo:#4d53c4;
  --ink:#1f1f24;
  --muted:#4a4a52;
  --line:#e3e3e3;
  --card-img:#f1f1f1;
}
*{box-sizing:border-box;margin:0;padding:0}
html,body{width:1200px;height:2222px;overflow:hidden}
body{font-family:"Inter",sans-serif;color:var(--ink);background:#fff;position:relative}
.site-header{position:absolute;left:0;top:0;width:1200px;height:128px;background:var(--header-bg);box-shadow:0 2px 4px rgba(0,0,0,.06)}
.brand-mark{position:absolute;left:22px;top:40px;display:flex;align-items:center;gap:8px;font-size:18px;font-weight:600;color:#1d3f8f}
.brand-mark span.sq{width:18px;height:18px;background:#1d3f8f}
.main-nav{position:absolute;left:205px;top:20px;font-size:15.5px;font-weight:500}
.main-nav a{position:absolute;white-space:nowrap;color:var(--ink);text-decoration:none;display:flex;align-items:center;gap:6px}
.main-nav a.active{color:var(--accent);font-weight:600}
.search{position:absolute;left:205px;top:60px;width:550px;height:38px;border:1px solid #cfcfcf;border-radius:19px;background:#fff;display:flex;align-items:center;padding-left:14px;gap:12px;font-size:11.5px;color:#888}
.pill{position:absolute;top:24px;height:28px;border:1px solid #cfcfcf;border-radius:14px;display:flex;align-items:center;justify-content:center;gap:6px;font-size:13.5px;background:var(--header-bg)}
.cart-badge{position:absolute;top:-8px;right:4px;width:14px;height:14px;border-radius:7px;background:var(--accent);color:#fff;font-size:9px;display:flex;align-items:center;justify-content:center}
.page-title{position:absolute;left:41px;top:170px;display:flex;align-items:center;gap:10px;font-size:26px;font-weight:500}
.back{width:31px;height:31px;border-radius:50%;background:#eee;display:flex;align-items:center;justify-content:center}
.filter{position:absolute;top:189px;height:27px;border:1px solid var(--accent);border-radius:14px;color:var(--accent);font-size:12px;display:flex;align-items:center;justify-content:center;gap:5px}
.latest{position:absolute;left:3px;top:227px;width:1197px;height:705px;background:linear-gradient(90deg,#fffbe0,#ffffff 60%,#fffde8)}
.section-title{position:absolute;left:69px;font-size:21px;font-weight:500}
.grid{position:absolute;left:67px;width:1066px;display:grid;grid-template-columns:repeat(5,199px);column-gap:17.5px;row-gap:18px}
.card{height:280px;background:#fff;border:1px solid var(--line);border-radius:3px;overflow:hidden;display:flex;flex-direction:column;position:relative}
.card-img{height:166px;background:var(--card-img)}
.badge{position:absolute;top:6px;right:6px;width:32px;height:33px;background:var(--accent);border-radius:5px;color:#fff;text-align:center;font-weight:600;font-size:13px;line-height:15px;padding-top:4px}
.badge small{display:block;font-size:7.5px;font-weight:400;line-height:9px}
.card-body{padding:10px 10px 0;flex:1}
.card-title{font-size:12px;line-height:14.5px;color:var(--muted)}
.card-title.clamp{white-space:nowrap;overflow:hidden}
.card-title.clamp span{display:block;overflow:hidden;text-overflow:ellipsis}
.price{color:var(--accent);font-size:15px;font-weight:500;margin-top:10px}
.card-actions{display:flex;height:25px;font-size:11px}
.card-actions .add{width:99px;background:var(--indigo);color:#fff;display:flex;align-items:center;justify-content:center;gap:6px}
.card-actions .info{flex:1;background:#f3f3f3;color:var(--muted);display:flex;align-items:center;justify-content:center;gap:5px}
.see-all{position:absolute;left:1063px;top:976px;width:70px;height:21px;border:1px solid var(--accent);border-radius:11px;color:var(--accent);font-size:11px;display:flex;align-items:center;justify-content:center;gap:5px}
.hero{position:absolute;left:0;top:1338px;width:1200px;height:463px}
.hero-art{position:absolute;inset:0;background:linear-gradient(160deg,#5a8a91 0%,#3f6e76 45%,#c9742f 75%,#e8e1d6 100%)}
.hero-box{position:absolute;left:526px;top:208px;width:632px;height:214px;background:#fffdee;border-radius:8px;text-align:center}
.hero-box h2{font-size:26px;font-weight:500;margin-top:34px;white-space:nowrap}
.hero-box p{font-size:17.5px;margin-top:16px}
.hero-box .cta{display:inline-block;margin-top:38px;width:130px;height:35px;line-height:35px;background:var(--accent);color:#fff;border-radius:3px;font-size:14px}
.site-footer{position:absolute;left:0;top:1804px;width:1200px;height:418px;background:linear-gradient(110deg,#e77d2e 0%,#1a0d0f 18%,#100c0e 45%,#8e1b29 62%,#c3413b 80%,#e36a3c 100%);color:#fff}
.footer-band{position:absolute;left:0;top:85px;width:1200px;height:249px;background:linear-gradient(90deg,rgba(10,10,12,.93),rgba(10,10,12,.9) 55%,rgba(60,10,20,.35))}
.fcol{position:absolute;text-align:center;font-size:12.5px}
.fcol h4{font-size:15.5px;font-weight:600;margin-bottom:16px}
.fcol p{line-height:27.5px}
.nl-input{width:300px;height:35px;background:#fff;border-radius:2px;color:#999;font-size:12px;line-height:35px}
.nl-btn{width:110px;height:33px;border:1.5px solid #fff;border-radius:2px;line-height:30px;font-weight:600;font-size:12px;margin:22px auto 0}
.social{display:flex;gap:12px;justify-content:center;margin-top:10px}
.social span{width:31px;height:31px;border:1.5px solid #fff;border-radius:50%}
</style>
</head>
<body>
<header class="site-header">
  <div class="brand-mark"><span class="sq"></span>PelvixRails</div>
  <nav class="main-nav">
    <a class="active" style="left:0;top:0"><svg width="16" height="15" viewBox="0 0 16 15"><path d="M8 0 0 7h2v8h4v-5h4v5h4V7h2z" fill="#ea4340"/></svg>Home</a>
    <a style="left:103px;top:0">Brand <svg width="10" height="6"><path d="M1 1l4 4 4-4" stroke="#222" fill="none" stroke-width="1.5"/></svg></a>
    <a style="left:200px;top:0">Scale <svg width="10" height="6"><path d="M1 1l4 4 4-4" stroke="#222" fill="none" stroke-width="1.5"/></svg></a>
    <a style="left:297px;top:0">Category <svg width="10" height="6"><path d="M1 1l4 4 4-4" stroke="#222" fill="none" stroke-width="1.5"/></svg></a>
    <a style="left:420px;top:0">Company <svg width="10" height="6"><path d="M1 1l4 4 4-4" stroke="#222" fill="none" stroke-width="1.5"/></svg></a>
  </nav>
  <div class="search"><svg width="17" height="17" viewBox="0 0 17 17"><circle cx="7" cy="7" r="5.5" stroke="#222" stroke-width="1.8" fill="none"/><path d="M11 11l5 5" stroke="#222" stroke-width="1.8"/></svg>Search Products, Brands, Scales...</div>
  <div class="pill" style="left:992px;width:75px"><svg width="15" height="14" viewBox="0 0 15 14"><path d="M1 1h2l2 8h8l1-6H4" stroke="#222" fill="none" stroke-width="1.4"/><circle cx="6" cy="12" r="1.2" fill="#222"/><circle cx="12" cy="12" r="1.2" fill="#222"/></svg>Cart<span class="cart-badge">4</span></div>
  <div class="pill" style="left:1091px;width:84px"><svg width="14" height="14" viewBox="0 0 14 14"><circle cx="7" cy="7" r="6" stroke="#222" fill="none" stroke-width="1.3"/><circle cx="7" cy="5.5" r="2" stroke="#222" fill="none" stroke-width="1.3"/></svg>Log in</div>
</header>

<div class="page-title"><span class="back"><svg width="8" height="12"><path d="M6 1 1 6l5 5" stroke="#222" fill="none" stroke-width="2"/></svg></span>Locomotives</div>
<div class="filter" style="left:832px;width:101px">Availability <svg width="9" height="6"><path d="M1 1l3.5 3.5L8 1" stroke="#ea4340" fill="none" stroke-width="1.3"/></svg></div>
<div class="filter" style="left:942px;width:74px">Brand <svg width="9" height="6"><path d="M1 1l3.5 3.5L8 1" stroke="#ea4340" fill="none" stroke-width="1.3"/></svg></div>
<div class="filter" style="left:1027px;width:106px"><svg width="13" height="11"><path d="M0 2h13M0 5.5h13M0 9h13" stroke="#ea4340" stroke-width="1.2"/><circle cx="4" cy="2" r="1.6" fill="#fff" stroke="#ea4340"/><circle cx="9" cy="5.5" r="1.6" fill="#fff" stroke="#ea4340"/><circle cx="5" cy="9" r="1.6" fill="#fff" stroke="#ea4340"/></svg>More Filter</div>

<section class="latest"></section>
<h3 class="section-title" style="top:268px">Latest Products</h3>
<div class="grid" style="top:311px">
  <article class="card"><div class="card-img" role="img" aria-label="Blue passenger coach model" style="background:linear-gradient(150deg,#f2f2f2 30%,#3c5ea8 50%,#2b3b6a 65%,#f2f2f2 80%)"></div><div class="badge">HO<small>Scale</small></div><div class="card-body"><p class="card-title">Tobias The Tank Engine™ With DCC Sound &amp; Moving Eyes</p><p class="price">€299</p></div><div class="card-actions"><span class="add">🛒 Add to Cart</span><span class="info">ⓘ More Info</span></div></article>
  <article class="card"><div class="card-img" role="img" aria-label="Green diesel locomotive model" style="background:linear-gradient(170deg,#f2f2f2 35%,#8bc43c 50%,#2e2e2e 62%,#f2f2f2 75%)"></div><div class="badge">HO<small>Scale</small></div><div class="card-body"><p class="card-title">HO PRIME SILVER PS-40 GRAINFIELD</p><p class="price">€399</p></div><div class="card-actions"><span class="add">🛒 Add to Cart</span><span class="info">ⓘ More Info</span></div></article>
  <article class="card"><div class="card-img" role="img" aria-label="Grey covered hopper car model" style="background:linear-gradient(180deg,#f2f2f2 10%,#c9c9c9 30%,#b3b3b3 60%,#3a3a3a 78%,#f2f2f2 90%)"></div><div class="badge">HO<small>Scale</small></div><div class="card-body"><p class="card-title">Chemical Tank Car - Allbright Chemical/Arden</p><p class="price">€259</p></div><div class="card-actions"><span class="add">🛒 Add to Cart</span><span class="info">ⓘ More Info</span></div></article>
  <article class="card"><div class="card-img" role="img" aria-label="Passenger car end view model" style="background:linear-gradient(90deg,#2a2a2e 40%,#8aa4c6 60%,#c8413a 85%)"></div><div class="badge">HO<small>Scale</small></div><div class="card-body"><p class="card-title">Chemical Tank Car - Hollis Chemicals</p><p class="price">€99</p></div><div class="card-actions"><span class="add">🛒 Add to Cart</span><span class="info">ⓘ More Info</span></div></article>
  <article class="card"><div class="card-img" role="img" aria-label="Orange boxcar model" style="background:linear-gradient(180deg,#f2f2f2 15%,#c4582f 30%,#8d3c22 65%,#2e2e2e 78%,#f2f2f2 90%)"></div><div class="badge">HO<small>Scale</small></div><div class="card-body"><p class="card-title clamp"><span>PREORDER MTR Prime O</span><span>41-73620 Flat Car With Prime..</span></p><p class="price">€199</p></div><div class="card-actions"><span class="add">🛒 Add to Cart</span><span class="info">ⓘ More Info</span></div></article>

  <article class="card"><div class="card-img" role="img" aria-label="Holiday boxcar model" style="background:linear-gradient(180deg,#f2f2f2 10%,#1f5a45 30%,#a83a33 50%,#1f5a45 70%,#3a3a3a 80%,#f2f2f2 92%)"></div><div class="badge">HO<small>Scale</small></div><div class="card-body"><p class="card-title clamp"><span>Waldner Mainline HO 31460 50'</span><span>100-Ton 4-Bay Hopper, Lakeshore..</span></p><p class="price">€299</p></div><div class="card-actions"><span class="add">🛒 Add to Cart</span><span class="info">ⓘ More Info</span></div></article>
  <article class="card"><div class="card-img" role="img" aria-label="Blue passenger coach model" style="background:linear-gradient(150deg,#f2f2f2 30%,#3c5ea8 50%,#2b3b6a 65%,#f2f2f2 80%)"></div><div class="badge">HO<small>Scale</small></div><div class="card-body"><p class="card-title">First Appearing On American Railroads In The Late 1940s</p><p class="price">€399</p></div><div class="card-actions"><span class="add">🛒 Add to Cart</span><span class="info">ⓘ More Info</span></div></article>
  <article class="card"><div class="card-img" role="img" aria-label="Blue and red passenger car model" style="background:linear-gradient(180deg,#f2f2f2 30%,#2f4f8a 40%,#d0d0d0 50%,#c8413a 60%,#f2f2f2 70%)"></div><div class="badge">HO<small>Scale</small></div><div class="card-body"><p class="card-title">Chemical Tank Cars Provided A Safe And Efficient Means</p><p class="price">€299</p></div><div class="card-actions"><span class="add">🛒 Add to Cart</span><span class="info">ⓘ More Info</span></div></article>
  <article class="card"><div class="card-img" role="img" aria-label="Black steam locomotive model" style="background:linear-gradient(180deg,#f2f2f2 20%,#1f1f22 35%,#2a2a2e 65%,#c8c8c8 78%,#f2f2f2 90%)"></div><div class="badge">HO<small>Scale</small></div><div class="card-body"><p class="card-title">Edmund (With Moving Eyes) (HO Scale)</p><p class="price">€99</p></div><div class="card-actions"><span class="add">🛒 Add to Cart</span><span class="info">ⓘ More Info</span></div></article>
  <article class="card"><div class="card-img" role="img" aria-label="Black steam locomotive front view model" style="background:radial-gradient(circle at 40% 45%,#1f1f22 40%,#f2f2f2 75%)"></div><div class="badge">HO<small>Scale</small></div><div class="card-body"><p class="card-title">Pippin The Small Engine™ With DCC Sound &amp; Moving Eyes</p><p class="price">€199</p></div><div class="card-actions"><span class="add">🛒 Add to Cart</span><span class="info">ⓘ More Info</span></div></article>
</div>

<h3 class="section-title" style="top:973px">Featured Collection</h3>
<div class="see-all">See All <svg width="6" height="9"><path d="M1 1l3.5 3.5L1 8" stroke="#ea4340" fill="none" stroke-width="1.3"/></svg></div>
<div class="grid" style="top:1015px">
  <article class="card"><div class="card-img" role="img" aria-label="Black steam locomotive model" style="background:linear-gradient(180deg,#f2f2f2 20%,#1f1f22 35%,#2a2a2e 65%,#c8c8c8 78%,#f2f2f2 90%)"></div><div class="badge">HO<small>Scale</small></div><div class="card-body"><p class="card-title">Edmund (With Moving Eyes) (HO Scale)</p><p class="price">€99</p></div><div class="card-actions"><span class="add">🛒 Add to Cart</span><span class="info">ⓘ More Info</span></div></article>
  <article class="card"><div class="card-img" role="img" aria-label="Holiday boxcar model" style="background:linear-gradient(180deg,#f2f2f2 10%,#1f5a45 30%,#a83a33 50%,#1f5a45 70%,#3a3a3a 80%,#f2f2f2 92%)"></div><div class="badge">HO<small>Scale</small></div><div class="card-body"><p class="card-title">Waldner Mainline HO 31460 50' 100-Ton 4-Bay Hopper, Lakeshore &amp; Eastern Plains</p><p class="price">€299</p></div><div class="card-actions"><span class="add">🛒 Add to Cart</span><span class="info">ⓘ More Info</span></div></article>
  <article class="card"><div class="card-img" role="img" aria-label="Blue and red passenger car model" style="background:linear-gradient(180deg,#f2f2f2 30%,#2f4f8a 40%,#d0d0d0 50%,#c8413a 60%,#f2f2f2 70%)"></div><div class="badge">HO<small>Scale</small></div><div class="card-body"><p class="card-title">Chemical Tank Cars Provided A Safe And Efficient Means</p><p class="price">€299</p></div><div class="card-actions"><span class="add">🛒 Add to Cart</span><span class="info">ⓘ More Info</span></div></article>
  <article class="card"><div class="card-img" role="img" aria-label="Black steam locomotive front view model" style="background:radial-gradient(circle at 40% 45%,#1f1f22 40%,#f2f2f2 75%)"></div><div class="badge">HO<small>Scale</small></div><div class="card-body"><p class="card-title">Pippin The Small Engine™ With DCC Sound &amp; Moving Eyes</p><p class="price">€199</p></div><div class="card-actions"><span class="add">🛒 Add to Cart</span><span class="info">ⓘ More Info</span></div></article>
  <article class="card"><div class="card-img" role="img" aria-label="Grey covered hopper car model" style="background:linear-gradient(180deg,#f2f2f2 10%,#c9c9c9 30%,#b3b3b3 60%,#3a3a3a 78%,#f2f2f2 90%)"></div><div class="badge">HO<small>Scale</small></div><div class="card-body"><p class="card-title">Chemical Tank Car - Allbright Chemical/Arden</p><p class="price">€259</p></div><div class="card-actions"><span class="add">🛒 Add to Cart</span><span class="info">ⓘ More Info</span></div></article>
</div>

<section class="hero">
  <div class="hero-art" role="img" aria-label="Orange and white modern train model on a teal backdrop"></div>
  <div class="hero-box">
    <h2>Prairie Pacific Early Contender (PX-7) - HO</h2>
    <p>Pre-order the latest models from PelvixRails</p>
    <span class="cta">Pre-Order Today</span>
  </div>
</section>

<footer class="site-footer">
  <div class="footer-band"></div>
  <div class="fcol" style="left:134px;top:143px;width:140px">
    <h4>FAQ</h4>
    <p>Company</p><p>Employment</p><p>Order History</p><p>Terms &amp; Services</p>
  </div>
  <div class="fcol" style="left:450px;top:146px;width:300px">
    <h4>Newsletter</h4>
    <div class="nl-input">Enter your email</div>
    <div class="nl-btn">Subscribe</div>
  </div>
  <div class="fcol" style="left:880px;top:130px;width:200px">
    <h4>General Information</h4>
    <p>+1 234 567 890</p><p>123 Main Street</p><p>City, State, Country</p>
    <div class="social"><span></span><span></span><span></span><span></span></div>
  </div>
</footer>
</body>
</html>
```